Lanternfield Drinks business cards

We need a business card design for our new logo. The company is modern, progressive, professional, yet approachable. The key products are ready to drink bottles and cans of coffee based beverages.
These cards will be a critical part of the first impression made by our sales organization, business development team, and all external facing personnel.
Card can be a vertical or horizontal orientation.

Target Market(s)

Customers, suppliers, business partners

Industry/Entity Type

Business

Contact Information for Business Card

Business cards should feature Company Name and Logo.

Font styles to use
Serif

Colors

Designer to choose colors to be used in the design.

Requirements
Must have
• Strong readability of Name, phone #, mobile number and email address.
• Job title, website url, Street Address, and other details can be secondary level readability.
Nice to have
• High impact, simplistic quality design.
• Ok to utilize the 'H in the box' separate from the company name

```html
<!DOCTYPE html>
<html lang="en">
<head>
<meta charset="utf-8">
<title>Lanternfield Drinks – Business Cards</title>
<link rel="stylesheet" href="https://fonts.googleapis.com/css2?family=Cinzel:wght@700&family=Lato:wght@400;700&display=swap">
<style>
  :root {
    --backdrop: #c8c6c7;
    --card: #000000;
    --orange: #f05a28;
    --amber: #f7a21b;
    --ink-light: #ffffff;
    --rule: #8a8a8a;
  }
  * { margin: 0; padding: 0; box-sizing: border-box; }
  html, body { width: 1200px; height: 900px; overflow: hidden; }
  body {
    background: var(--backdrop);
    position: relative;
    font-family: "Lato", Arial, sans-serif;
  }
  .card {
    position: absolute;
    width: 478px;
    height: 295px;
    background: var(--card);
    box-shadow: 2px 3px 4px rgba(0,0,0,0.35);
    overflow: hidden;
  }
  .card--front { left: 116px; top: 275px; border-radius: 0 48px 0 48px; }
  .card--back  { left: 622px; top: 276px; border-radius: 48px 0 48px 0; }

  .brand-square {
    position: absolute;
    border: 3px solid var(--orange);
  }
  .brand-name {
    position: absolute;
    font-family: "Cinzel", Georgia, serif;
    font-weight: 700;
    color: var(--orange);
    text-align: center;
    white-space: nowrap;
    line-height: 1;
  }
  .card--front .brand-square { left: 300px; top: 25px; width: 68px; height: 67px; }
  .card--front .brand-name { left: 209px; width: 250px; top: 110px; font-size: 18px; }
  .card--back .brand-square { left: 186px; top: 52px; width: 105px; height: 105px; border-width: 4px; }
  .card--back .brand-name { left: 39px; width: 400px; top: 184px; font-size: 28px; }

  .person-name {
    position: absolute; left: 22px; top: 171px;
    font-size: 20px; font-weight: 700; color: var(--orange); letter-spacing: 0.2px;
  }
  .name-rule {
    position: absolute; left: 171px; top: 183px; width: 278px; height: 1px;
    background: var(--rule);
  }
  .job-title {
    position: absolute; left: 23px; top: 195px;
    font-size: 14px; color: var(--amber);
  }
  .address {
    position: absolute; left: 22px; top: 219px;
    font-size: 14px; color: var(--ink-light); line-height: 17.5px;
  }
  .address .line { padding-left: 13px; }
  .address .pin { position: absolute; left: 0; top: 3px; }
  .contacts {
    position: absolute; right: 26px; top: 205px;
    list-style: none; font-size: 14px; color: var(--ink-light);
    text-align: right; line-height: 16.6px;
  }
  .contacts li { display: flex; justify-content: flex-end; align-items: center; gap: 5px; }
  .contacts svg { width: 11px; height: 11px; flex: none; }
</style>
</head>
<body>

  <section class="card card--front" aria-label="Card front">
    <div class="brand-square"></div>
    <div class="brand-name">LANTERNFIELD DRINKS</div>

    <div class="person-name">LORUM SMITH</div>
    <div class="name-rule"></div>
    <div class="job-title">Managing Director</div>

    <div class="address">
      <svg class="pin" width="9" height="12" viewBox="0 0 9 12"><path d="M4.5 0C2 0 0 2 0 4.4 0 7.5 4.5 12 4.5 12S9 7.5 9 4.4C9 2 7 0 4.5 0zm0 6.2a1.8 1.8 0 1 1 0-3.6 1.8 1.8 0 0 1 0 3.6z" fill="var(--orange)"/></svg>
      <div class="line">421, Address line here,</div>
      <div class="line">Dummy Code, 45452</div>
      <div class="line">Country Name</div>
    </div>

    <ul class="contacts">
      <li>444 555 6688
        <svg viewBox="0 0 10 10"><path d="M1 3.5C1 2 2.5 1 5 1s4 1 4 2.5L7.5 4.2 6.5 3v-.5h-3V3L2.5 4.2zM2.5 5h5L9 9H1z" fill="var(--orange)"/></svg>
      </li>
      <li>888 555 4433
        <svg viewBox="0 0 10 10"><rect x="2.5" y="0.5" width="5" height="9" rx="1" fill="none" stroke="var(--orange)" stroke-width="1.2"/><rect x="4.3" y="7.4" width="1.4" height="1" fill="var(--orange)"/></svg>
      </li>
      <li>info@webname.com
        <svg viewBox="0 0 10 10"><rect x="0.5" y="2" width="9" height="6.5" fill="var(--orange)"/><path d="M0.8 2.3 5 5.8l4.2-3.5" fill="none" stroke="#000" stroke-width="0.9"/></svg>
      </li>
      <li>www.webaddress.com
        <svg viewBox="0 0 10 10"><circle cx="5" cy="5" r="4.5" fill="var(--orange)"/><path d="M3 3.5c1 0 1.5.8 1.2 1.6-.3.8.5 1.2.9 2M6.5 2c.3.8 1.3.9 1.8.6" fill="none" stroke="#000" stroke-width="0.9"/></svg>
      </li>
    </ul>
  </section>

  <section class="card card--back" aria-label="Card back">
    <div class="brand-square"></div>
    <div class="brand-name">LANTERNFIELD DRINKS</div>
  </section>

</body>
</html>
```